Women's Health Company needs business card

We need a business card for a USA based women's health care company. We use digital technology to enhance therapy prescribed by clinicians for their patients

```html
<!DOCTYPE html>
<html lang="en">
<head>
<meta charset="utf-8">
<title>Lunera Health — Business Card</title>
<link rel="stylesheet" href="https://fonts.googleapis.com/css2?family=Montserrat:wght@400;600&display=swap">
<style>
  :root {
    --backdrop: #5e4331;
    --card-white: #ffffff;
    --brand-purple: #8e559f;
    --brand-teal: #72bfbb;
    --text-grey: #5a5a5a;
  }
  * { box-sizing: border-box; margin: 0; padding: 0; }
  html, body {
    width: 1200px;
    height: 1200px;
    overflow: hidden;
    background: var(--backdrop);
    font-family: "Montserrat", sans-serif;
  }
  .canvas {
    position: relative;
    width: 1200px;
    height: 1200px;
  }
  .card {
    position: absolute;
    left: 173px;
    width: 854px;
    height: 486px;
    border-radius: 26px;
    overflow: hidden;
  }
  .card--front { top: 87px; background: var(--card-white); }
  .card--back  { top: 627px; background: var(--brand-purple); }

  .brand-name {
    font-weight: 400;
    letter-spacing: 1px;
    white-space: nowrap;
  }
  .card--front .brand-name {
    position: absolute;
    left: 62px;
    top: 206px;
    width: 382px;
    text-align: center;
    font-size: 50px;
    color: var(--brand-teal);
  }
  .divider {
    position: absolute;
    left: 480px;
    top: 141px;
    width: 2px;
    height: 204px;
    background: var(--brand-purple);
  }
  .contact {
    position: absolute;
    left: 518px;
    top: 133px;
    color: var(--text-grey);
    font-size: 20.5px;
    line-height: 1.3;
  }
  .contact__name {
    font-weight: 600;
    font-size: 34px;
    color: var(--brand-purple);
    letter-spacing: 0.5px;
    line-height: 1.1;
  }
  .contact__role { margin-bottom: 8px; }
  .contact__address { margin-bottom: 8px; line-height: 1.3; }
  .contact__line {
    display: flex;
    align-items: center;
    gap: 8px;
    line-height: 1.35;
  }
  .contact__icon { width: 15px; height: 15px; flex: none; }
  .card__stripe {
    position: absolute;
    left: 0;
    right: 0;
    bottom: 44px;
    height: 6px;
    background: var(--brand-teal);
  }
  .card__band {
    position: absolute;
    left: 0;
    right: 0;
    bottom: 0;
    height: 38px;
    background: var(--brand-purple);
  }
  .card--back .brand-name {
    position: absolute;
    left: 0;
    right: 0;
    top: 200px;
    text-align: center;
    font-size: 66px;
    color: var(--card-white);
  }
</style>
</head>
<body>
<div class="canvas">

  <section class="card card--front">
    <div class="brand-name">Lunera Health</div>
    <div class="divider"></div>
    <div class="contact">
      <div class="contact__name">DANIEL REYES</div>
      <div class="contact__role">Director</div>
      <div class="contact__address">1175 Harbor Lane<br>Albany, NY 12207</div>
      <div class="contact__line">
        <svg class="contact__icon" viewBox="0 0 16 16"><path d="M4 1.5 L6 5 L4.6 6.4 C5.4 8.4 7.2 10.4 9.4 11.4 L10.8 10 L14 12.2 L12.6 14.4 C7 14 2 9 1.8 3 Z" fill="none" stroke="var(--brand-purple)" stroke-width="1.5" stroke-linejoin="round"/></svg>
        <span>555.014.2290</span>
      </div>
      <div class="contact__line">
        <svg class="contact__icon" viewBox="0 0 16 16"><rect x="1.5" y="3.5" width="13" height="9" fill="none" stroke="var(--brand-purple)" stroke-width="1.5"/><path d="M1.5 3.5 L8 9 L14.5 3.5" fill="none" stroke="var(--brand-purple)" stroke-width="1.5"/></svg>
        <span>hello@lunerahealth.com</span>
      </div>
      <div class="contact__line">
        <svg class="contact__icon" viewBox="0 0 16 16"><circle cx="8" cy="8" r="6.5" fill="none" stroke="var(--brand-purple)" stroke-width="1.3"/><ellipse cx="8" cy="8" rx="3" ry="6.5" fill="none" stroke="var(--brand-purple)" stroke-width="1.1"/><path d="M1.5 8 H14.5 M2.6 4.6 H13.4 M2.6 11.4 H13.4" stroke="var(--brand-purple)" stroke-width="1.1"/></svg>
        <span>www.lunerahealth.com</span>
      </div>
    </div>
    <div class="card__stripe"></div>
    <div class="card__band"></div>
  </section>

  <section class="card card--back">
    <div class="brand-name">Lunera Health</div>
  </section>

</div>
</body>
</html>
```